Stationery/Logo design for law office

Hello, I am looking for a logo and stationery design for my law office. I am a solo practitioner in New York. I would like the logo to be based around my initials: KRW. Original, I know!
Hello:

I need (1) the logo, (2) a letterhead/stationery design, and (3) an envelope design. I would like the logo to be BLUE. Other than that, I am open and looking forward to seeing different designs.

For my privacy, I am using a sample name/information (the real info will be provided to the winning designer). I would like the logo to consist of the KRW design and the words "Marcus R. Welton Law Office." I plan to use a version with both of those elements, as well as just the KRW design alone.

The information that should go in the letterhead and envelope design is the following:

Marcus R. Welton Law Office
742 Alder Lane
Suite 318
Larkmont, New York 10592
212-384-7265
www.weltonlegalfirm.example

I am open to different formats (changing the order of my contact info, writing the phone number without dashes, etc.); I know it's not a ton of content but I would like it to look good -- and I'm open to both classic and more modern looks.

Note that the sample colors I selected are not meant to be exclusive -- there aren't a ton of options.

Thanks in advance!

• I am leaning toward a design just based on my initials, but I am open to ideas -- just nothing trite like scales of justice or a gavel.

```html
<!DOCTYPE html>
<html lang="en">
<head>
<meta charset="utf-8">
<title>Marcus R. Welton Law Office — Stationery</title>
<link rel="stylesheet" href="https://fonts.googleapis.com/css2?family=Cinzel:wght@500&family=Tinos&display=swap">
<style>
  :root {
    --navy: #1c4f7c;
    --paper: #ffffff;
    --rule: #5f82a3;
    --ink: #1c4f7c;
    --backdrop: #e9eef2;
    --name-font: "Cinzel", serif;
    --text-font: "Tinos", serif;
  }
  * { box-sizing: border-box; margin: 0; padding: 0; }
  html, body { width: 1200px; height: 1000px; overflow: hidden; }
  body { background: var(--backdrop); position: relative; font-family: var(--text-font); color: var(--ink); }

  .wordmark { font-family: var(--name-font); font-weight: 500; color: var(--navy); display: flex; align-items: center; gap: 12px; line-height: 1.15; }
  .wordmark .mark-square { width: 14px; height: 14px; background: currentColor; flex: none; }
  .wordmark--light { color: var(--paper); }

  .address { font-style: normal; font-size: 11px; line-height: 1.5; color: var(--ink); white-space: nowrap; }

  /* Letterhead */
  .letterhead { position: absolute; left: 60px; top: 120px; width: 520px; height: 740px; background: var(--paper); box-shadow: 0 2px 10px rgba(20,50,80,.12); }
  .letterhead__header { position: absolute; left: 0; top: 0; width: 100%; height: 140px; border-bottom: 1px solid var(--rule); }
  .letterhead__wordmark { position: absolute; left: 36px; bottom: 22px; font-size: 17px; width: 220px; }
  .letterhead__contact { position: absolute; right: 0; top: 0; width: 190px; height: 100%; border-left: 1px solid var(--rule); padding: 22px 0 0 14px; font-size: 10px; }

  /* Logo lockup */
  .logo-lockup { position: absolute; left: 660px; top: 60px; width: 460px; height: 160px; background: var(--paper); display: flex; align-items: center; justify-content: center; }
  .logo-lockup .wordmark { font-size: 26px; }

  /* Business card */
  .business-card { position: absolute; left: 660px; top: 260px; width: 350px; height: 200px; background: var(--navy); display: flex; align-items: center; justify-content: center; box-shadow: 0 2px 10px rgba(20,50,80,.18); }
  .business-card .wordmark { font-size: 15px; }

  /* Envelope */
  .envelope { position: absolute; left: 660px; top: 500px; width: 460px; height: 360px; background: var(--paper); box-shadow: 0 2px 10px rgba(20,50,80,.12); }
  .envelope__flap-line { position: absolute; left: 350px; top: 0; width: 1px; height: 100%; background: var(--rule); }
  .envelope__wordmark { position: absolute; left: 36px; top: 36px; font-size: 16px; width: 260px; }
  .envelope__return { position: absolute; left: 40px; bottom: 36px; font-size: 12px; }
</style>
</head>
<body>

  <section class="letterhead" aria-label="Letterhead">
    <header class="letterhead__header">
      <div class="wordmark letterhead__wordmark"><span class="mark-square"></span><span>Marcus R. Welton<br>Law Office</span></div>
      <address class="address letterhead__contact">
        742 Alder Lane<br>
        Suite 318<br>
        Larkmont, New York 10592<br>
        212-384-7265<br>
        www.weltonlegalfirm.example
      </address>
    </header>
  </section>

  <section class="logo-lockup" aria-label="Logo">
    <div class="wordmark"><span class="mark-square"></span><span>Marcus R. Welton<br>Law Office</span></div>
  </section>

  <section class="business-card" aria-label="Business card">
    <div class="wordmark wordmark--light"><span class="mark-square"></span><span>Marcus R. Welton<br>Law Office</span></div>
  </section>

  <section class="envelope" aria-label="Envelope">
    <div class="wordmark envelope__wordmark"><span class="mark-square"></span><span>Marcus R. Welton<br>Law Office</span></div>
    <address class="address envelope__return">
      742 Alder Lane<br>
      Suite 318<br>
      Larkmont, New York 10592<br>
      212-384-7265<br>
      www.weltonlegalfirm.example
    </address>
    <div class="envelope__flap-line"></div>
  </section>

</body>
</html>
```